Real Estate "For Sale" Sign for a Colorado Real Estate Company

I need a sign for my Real Estate Company and the size needs to be 24inches by 24inches when printed on metal.
Logo is attached and would like to keep it modern and simple. We are a small town and I am not looking for a new age, industrial design. The concept needs to have the following attributes:

- Logo placed on sign
- Text "For Sale"
- Text "Reid Calloway" and my phone number "720-555-0143" (I would need any font package you use so that I can edit my number if that changes)
- Text "www.reid-calloway.example"
Im open to other attributes as well!

Target Market(s)

General Public driving around town.

Industry/Entity Type

Real Estate Agent

Requirements
Must have
• Logo and the colors must not be too busy. Contact Info very clear.

```html
<!DOCTYPE html>
<html lang="en">
<head>
<meta charset="utf-8">
<title>For Sale Sign – Cedar Ridge Realty</title>
<link href="https://fonts.googleapis.com/css2?family=Cinzel:wght@600&family=Fira+Sans:wght@600&display=swap" rel="stylesheet">
<style>
  :root {
    --page-bg: #ffffff;
    --sign-bg: #e6e7e8;
    --band-blue: #2478b5;
    --band-shadow: #1b5c8c;
    --ink-navy: #173c5c;
  }
  html, body {
    margin: 0;
    padding: 0;
    width: 1200px;
    height: 1000px;
    overflow: hidden;
    background: var(--page-bg);
  }
  .sign {
    position: absolute;
    left: 200px;
    top: 100px;
    width: 800px;
    height: 800px;
    background: var(--sign-bg);
    overflow: hidden;
  }
  .sign__band {
    position: absolute;
    left: 0;
    top: 0;
    width: 220px;
    height: 800px;
  }
  .sign__content {
    position: absolute;
    left: 190px;
    right: 20px;
    top: 0;
    bottom: 0;
    display: flex;
    flex-direction: column;
    align-items: center;
    color: var(--ink-navy);
    text-align: center;
  }
  .sign__headline {
    margin-top: 70px;
    font-family: "Cinzel", serif;
    font-weight: 600;
    font-size: 62px;
    letter-spacing: 2px;
    line-height: 1;
  }
  .brand {
    margin-top: 70px;
    display: flex;
    flex-direction: row;
    align-items: center;
    gap: 14px;
    font-family: "Fira Sans", sans-serif;
    font-weight: 600;
    color: var(--ink-navy);
  }
  .brand__mark {
    width: 24px;
    height: 24px;
    background: var(--band-blue);
  }
  .brand__name {
    font-size: 36px;
    line-height: 1;
  }
  .agent {
    margin-top: 80px;
    font-family: "Fira Sans", sans-serif;
    font-weight: 600;
    line-height: 1;
  }
  .agent__name {
    font-size: 80px;
  }
  .agent__phone {
    margin-top: 40px;
    font-size: 66px;
    letter-spacing: 2px;
  }
  .agent__web {
    margin-top: 90px;
    font-size: 38px;
  }
</style>
</head>
<body>
  <main class="sign">
    <svg class="sign__band" viewBox="0 0 220 800" aria-hidden="true">
      <path fill="var(--band-shadow)" d="M0 0 H150 C110 150 175 280 165 420 C155 560 120 650 175 800 H0 Z"/>
      <path fill="var(--band-blue)" d="M0 0 H132 C92 150 157 280 147 420 C137 560 102 650 157 800 H0 Z"/>
    </svg>
    <section class="sign__content">
      <div class="sign__headline">FOR SALE</div>
      <div class="brand">
        <div class="brand__mark"></div>
        <div class="brand__name">Cedar Ridge Realty LLC</div>
      </div>
      <div class="agent">
        <div class="agent__name">Reid Calloway</div>
        <div class="agent__phone">720-555-0143</div>
        <div class="agent__web">www.reid-calloway.example</div>
      </div>
    </section>
  </main>
</body>
</html>
```